The Lune Fox Organic & Natural Soaps needs a good business card

I am sorry for the lack of direction or Scope of the project. I am new at this board.
This is my scope and requirements:
Business card project:
This is related to the Label project I also opened up. (The Lune Fox Organic & Natural Soaps is looking for label designs (along with the business card project (Contest) )
I have attached an initial draft at a logo I tried to come up with for a business card and labelling/marketing. I am hoping that you can take this logo and 'run with it' to finesse it, make it look unique and professional. I am open to new logo ideas.
I am a start up at home company making Organic and Natural Bar soaps, hand soaps, body washes.
All of my ingredients are organic or natural and will include natural essential oils, exfoliants, natural powders/colours, etc.
Some of the names are: Brambelle (feisty, energetic soap), Dunes (more of a sandalwood earthy tones with a sandalwood powder exfoliant), Frost (maybe changing this name - fresh scented), Plum Cedar (lemongrass/ginger, exfoliants), etc....
I am attaching the cardstock I am looking at for packaging as well - this might help with the business card aspect. I was originally just looking at plain kraft paper but am receiving samples of Vera Pindle coloured kraft paper. I may still print business cards on the plain kraft though.. not sure.
If you need more information, please let me know.
Moira
Business Card and Labels
I have come up with a basic logo that I like. If you can finesse it and provide a great business card, that would be great.
I am starting up an at home soap business that will include luxury organic bar soaps, luxury natural olive oil bar soaps, organic hand wash, natural olive oil based body wash. I will be selling online and at shows.
please find attached my logo idea that I would like to incorporate.
I am also looking at packaging/labelling ideas for the bar soaps (prefer kraft cardstock wrap) and labels for the various body washes (natural soap) and the hand washes (organic). The hand washes will be in 250ml square bottles and the body wash will be in tapered bottles (smaller at top going to bottom).
Please let me know if you need more info!
I am also looking for packaging (label design for hand soap/body wash bottles and label design for organic/natural soaps)
This Project coincides with the business card project I also posted: there are 2 projects related - 1) business cards, 2) labels for organic hand wash, natural body wash, sticker label or design for kraft paper to package around luxury organic and natural soaps. I am not sure if a sticker would look nice or the design for the thick kraft paper.
Thank you!
Business card project:
This is related to the Label project I also opened up. (The Lune Fox Organic & Natural Soaps is looking for label designs (along with the business card proje (Contest) )
I have attached an initial draft at a logo I tried to come up with for a business card and labelling/marketing. I am hoping that you can take this logo and 'run with it' to finesse it, make it look unique and professional.
Moira
Hello; I just wanted to let everyone know that if you feel that this
brand needs a different logo, I am open to ideas (if you don't think the
one I started with is ok). I am coming to the experts here!
Just to confirm also - this is related to the label/packaging project, therefore, there are 2 projects, 2 payments! :)
Cheers

```html
<!DOCTYPE html>
<html lang="en">
<head>
<meta charset="utf-8">
<title>The Lune Fox – Business Card</title>
<link href="https://fonts.googleapis.com/css2?family=Arvo:wght@700&family=Patrick+Hand&display=swap" rel="stylesheet">
<style>
  :root {
    --page: #ffffff;
    --kraft: #e9dfd2;
    --kraft-light: #f4eee6;
    --orchid: #d4a3cf;
    --slate: #8e8e91;
    --ink-light: #ffffff;
  }
  html, body {
    margin: 0;
    width: 1200px;
    height: 1000px;
    overflow: hidden;
    background: var(--page);
  }
  .canvas {
    position: relative;
    width: 1200px;
    height: 1000px;
  }
  .card {
    position: absolute;
    left: 196px;
    width: 797px;
    height: 449px;
    background: var(--kraft);
    overflow: hidden;
    box-shadow: 4px 8px 10px rgba(0,0,0,0.35);
  }
  .card--front { top: 28px; }
  .card--back { top: 513px; }
  .stripe {
    position: absolute;
    left: 299px;
    top: 0;
    width: 95px;
    height: 100%;
    background: var(--orchid);
  }
  .brand {
    position: absolute;
    left: 0;
    width: 100%;
    text-align: center;
    font-family: "Arvo", serif;
    font-weight: 700;
    color: var(--slate);
    text-transform: uppercase;
    line-height: 1.05;
  }
  .card--front .brand { top: 118px; }
  .brand__name { display: block; font-size: 72px; letter-spacing: 2px; }
  .brand__tag { display: block; font-size: 24px; letter-spacing: 3px; margin-top: 22px; }
  .card--back .brand { top: 28px; }
  .card--back .brand__name { font-size: 36px; }
  .card--back .brand__tag { font-size: 14px; margin-top: 6px; letter-spacing: 2px; }
  .contact-frame {
    position: absolute;
    left: 189px;
    top: 92px;
    width: 420px;
    height: 270px;
  }
  .contact {
    position: absolute;
    left: 0;
    top: 160px;
    width: 797px;
    text-align: center;
    font-family: "Patrick Hand", cursive;
    font-size: 25px;
    line-height: 38px;
    color: var(--ink-light);
    margin: 0;
    font-style: normal;
  }
  .motto {
    position: absolute;
    font-family: "Patrick Hand", cursive;
    color: var(--kraft-light);
    font-size: 46px;
    line-height: 0.9;
    white-space: nowrap;
    opacity: 0.85;
  }
  .motto--pure { left: -10px; top: 150px; transform: rotate(90deg); }
  .motto--natural { left: 30px; top: 320px; transform: rotate(12deg); }
  .motto--organic { left: 600px; top: 40px; transform: rotate(180deg); text-align: right; }
  .motto--earth { left: 615px; top: 270px; transform: rotate(-80deg); }
</style>
</head>
<body>
<main class="canvas">

  <section class="card card--front">
    <div class="stripe"></div>
    <h1 class="brand">
      <span class="brand__name">The Lune Fox</span>
      <span class="brand__tag">Organic &amp; Natural Soaps</span>
    </h1>
  </section>

  <section class="card card--back">
    <div class="stripe"></div>

    <div class="motto motto--pure">handmade<br>+ pure</div>
    <div class="motto motto--natural">100%<br>Natural</div>
    <div class="motto motto--organic">organic<br>100%</div>
    <div class="motto motto--earth">earth<br>friendly</div>

    <svg class="contact-frame" viewBox="0 0 420 270" aria-hidden="true">
      <ellipse cx="210" cy="135" rx="191" ry="116" fill="var(--orchid)" stroke="var(--slate)" stroke-width="36"/>
    </svg>

    <div class="brand">
      <span class="brand__name">The Lune Fox</span>
      <span class="brand__tag">Organic &amp; Natural Soaps</span>
    </div>

    <address class="contact">
      Moira Hale, Owner<br>
      (416) 555-0148<br>
      Moira@thelunefox.ca<br>
      www.thelunefox.ca
    </address>
  </section>

</main>
</body>
</html>
```